依頼概要
本サービスの集客用FAXDMのデザインをお願い致します。

■コンセプト
「冷凍食品専門の物流倉庫!機能充実した最新設備が特長です」
※参考、物流倉庫サービスとは:https://www.kawanami-corp.jp/hokanbox/post-218

■ターゲット像:
★「冷凍食品・冷蔵食材」を扱う企業
・倉庫の確保がしたい物流会社も許容
→メーカー、卸売業者、EC業者などの区分は問わない。
→「飲食店」「食品メーカー」「農業」「卸会社」「物流会社」のリストに配布予定。

■ターゲットが保有するニーズ、あるいは課題
・品質管理のために高い冷凍機能が無いといけない。
・作業品質が悪く、納期遅延や破損・汚損が発生する。
・作業に忙殺されてしまっている。
・業績拡大に合わせて倉庫を拡張したい

■訴求するベネフィット:
①最新設備があって冷凍機能〇、その他の機能も〇。
②素晴らしい設備があるので、作業品質は万全。リソースも十分。
③埼玉県の好立地に広大な倉庫があります。首都圏にもスムーズに配送
④1個、1パレット、1日の小規模案件も喜んでご対応
⑤特定の期間のみ発送を強化してほしいなど柔軟に対応します。
→「衝撃のプライス!」のように価格を強く訴求することも可
→入庫料は無料

■その他、参考表現:
・埼玉県加須市に冷凍倉庫が出来ました
・保管商品を大募集しています
・1日からでも使えます
・費用は格安、保管費用は1パレット1日40円~(税込44円)から
(※パレットとは縦110cm×横110cmの保管単位です)
・ピッキングや発送業務も承ります

■必須の項目:
・相手の社名、担当者名、電話番号、メールアドレスを書く欄
・問い合わせ先として「受付センターの電話番号とFAX番号」を記載
TEL:0120-731-904/FAX:0280-47-9163
グリーンウェーブ受付センター 埼玉県加須市松葉912
受付時間9:00~18:00(日・3が日除く)

幅広く複数案の採用を考えています。
参考資料として、これまでのFAXDMデザインをお送り致します。

以上です。
■ 選んだ理由

弊社の雰囲気に合ったデザインを選ばせていただきました。FAXDM用ですので小さい字ではなく大きな字でわかりやすいデザインが良かったです。

■ 提案者全員のお礼・コメント

ありがとうございました。次回の制作予定ががありましたら積極的に本サイトを利用させていただきます。

```html
<!DOCTYPE html>
<html lang="ja">
<head>
<meta charset="utf-8">
<title>冷凍食品専門の物流倉庫 FAXDM</title>
<link rel="stylesheet" href="https://fonts.googleapis.com/css2?family=Noto+Sans+JP:wght@400;700;900&display=swap">
<style>
:root{
  --ink:#111;
  --paper:#fff;
  --grey:#e6e6e6;
  --mid:#9a9a9a;
}
*{margin:0;padding:0;box-sizing:border-box}
html,body{width:851px;height:1200px;overflow:hidden;background:var(--paper)}
body{font-family:"Noto Sans JP",sans-serif;color:var(--ink)}
.sheet{position:relative;width:851px;height:1200px}
.abs{position:absolute}

.features{top:20px;left:0;width:851px;height:150px}
.feature{position:absolute;top:0;width:150px;height:150px;border-radius:50%;background:var(--ink);color:var(--paper);
  display:flex;align-items:center;justify-content:center;text-align:center;font-weight:900;font-size:34px;line-height:1.15}

.headline{top:185px;left:30px;width:791px;height:125px;background:var(--ink)}
.headline .place{position:absolute;left:14px;top:12px;width:188px;height:100px;background:var(--paper);border-radius:6px;
  display:flex;align-items:center;justify-content:center;text-align:center;font-weight:900;font-size:38px;line-height:1.1}
.headline .lead{position:absolute;left:220px;top:6px;width:560px;text-align:center;color:var(--paper);font-weight:700;font-size:44px;line-height:58px}
.headline .title{position:absolute;left:220px;top:66px;width:560px;height:50px;background:var(--paper);border-radius:6px;
  text-align:center;font-weight:900;font-size:50px;line-height:50px;letter-spacing:1px}

.offer{top:325px;left:36px;width:779px;height:345px;border:3px solid var(--ink);border-radius:20px;overflow:hidden}
.offer .catch{position:absolute;left:0;top:0;width:510px;height:52px;background:var(--ink);color:var(--paper);
  font-weight:900;font-size:38px;line-height:52px;padding-left:18px;border-bottom-right-radius:14px}
.offer .service{position:absolute;left:36px;top:58px;font-weight:700;font-size:24px}
.offer .unit{position:absolute;left:18px;top:94px;font-weight:900;font-size:42px;line-height:52px;white-space:nowrap}
.offer .unit small{font-size:20px;font-weight:700}
.offer .unit span{font-size:30px}
.offer .recruit{position:absolute;left:12px;top:162px;width:184px;height:146px;background:var(--ink);color:var(--paper);
  font-weight:900;font-size:40px;line-height:1.35;white-space:nowrap;display:flex;flex-direction:column;align-items:center;justify-content:center;text-align:center}
.offer .price{position:absolute;left:206px;top:126px;font-weight:900;white-space:nowrap;line-height:1}
.offer .price b{font-size:200px;letter-spacing:-8px}
.offer .price span{font-size:62px}
.offer .quality{position:absolute;left:505px;top:4px;width:270px;height:150px}
.offer .workers{position:absolute;left:545px;top:140px;width:215px;height:185px;border-radius:16px;
  background:linear-gradient(180deg,#d8d8d8,#f2f2f2)}

.notice{top:684px;left:46px;width:220px;font-size:15px;font-weight:700;line-height:1.45}
.faxbar{top:680px;left:270px;width:548px;height:54px;background:var(--ink);color:var(--paper);
  font-weight:900;font-size:50px;line-height:54px;text-align:center;letter-spacing:1px}

.form{top:744px;left:30px;width:790px;border-collapse:collapse}
.form td{border:2px solid var(--ink);font-size:14px;font-weight:700;vertical-align:middle}
.form .label{width:82px;background:var(--grey);padding:0 8px;line-height:1.3}
.form .label.sub{width:90px}
.form .field{padding:4px 8px}
.form tr.tall td{height:62px}
.form tr.addr td{height:56px}
.form tr.addr .field{vertical-align:top}
.form tr.short td{height:40px}

.inquiry{top:958px;left:30px;width:790px;text-align:center;font-size:22px;font-weight:700;border-bottom:2px solid var(--ink);padding-bottom:4px}
.phone-icon{top:1012px;left:34px;width:86px;height:62px}
.tel{top:1002px;left:126px;font-weight:900;font-size:70px;line-height:82px;letter-spacing:1px;white-space:nowrap}
.hours{top:1010px;left:646px;width:176px;border:2px solid var(--ink);font-size:14px;font-weight:700;line-height:1.55;padding:6px 8px;white-space:nowrap}
.center{top:1092px;left:128px;font-size:19px;font-weight:700;white-space:nowrap}
.center span{margin-left:24px}
</style>
</head>
<body>
<div class="sheet">

  <div class="abs features">
    <div class="feature" style="left:14px">最新<br>設備</div>
    <div class="feature" style="left:182px">機能<br>充実</div>
    <div class="feature" style="left:350px">広大な<br>倉庫</div>
    <div class="feature" style="left:518px">お値段<br>格安</div>
    <div class="feature" style="left:686px">小規模<br>案件</div>
  </div>

  <div class="abs headline">
    <div class="place">埼玉県<br>加須市に</div>
    <div class="lead">冷凍食品専門の</div>
    <div class="title">物流倉庫誕生!</div>
  </div>

  <div class="abs offer">
    <div class="catch">1日からでも使えます</div>
    <div class="service">ピッキングや発送業務も承ります</div>
    <div class="unit">1パレット1日<small>（税込44円）</small><span>から</span></div>
    <div class="recruit"><span>保管商品</span><span>大募集</span></div>
    <div class="price"><b>40</b><span>円～</span></div>
    <svg class="quality" viewBox="0 0 270 150" aria-label="万全の品質管理">
      <defs><path id="arc" d="M30 140 Q135 -10 250 140"/></defs>
      <text font-family="Noto Sans JP, sans-serif" font-weight="900" font-size="34" fill="#111">
        <textPath href="#arc" startOffset="50%" text-anchor="middle">万全の品質管理</textPath>
      </text>
    </svg>
    <div class="workers" role="img" aria-label="台車で荷物を運ぶ作業員のイラスト"></div>
  </div>

  <div class="abs notice">下記に必要事項をご記入の上<br>送信してください。</div>
  <div class="abs faxbar">FAX.0280-47-9163</div>

  <table class="abs form">
    <tr class="tall">
      <td class="label">フリガナ<br>貴社名</td><td class="field"></td>
      <td class="label sub">フリガナ<br>ご担当者様</td><td class="field"></td>
    </tr>
    <tr class="addr">
      <td class="label">ご住所</td><td class="field" colspan="3">〒</td>
    </tr>
    <tr class="short">
      <td class="label">TEL</td><td class="field"></td>
      <td class="label sub">FAX</td><td class="field"></td>
    </tr>
    <tr class="short">
      <td class="label">mail</td><td class="field" colspan="3"></td>
    </tr>
  </table>

  <div class="abs inquiry">お電話でのお問い合わせ</div>
  <svg class="abs phone-icon" viewBox="0 0 88 64" aria-label="電話">
    <rect x="2" y="2" width="84" height="60" rx="10" fill="none" stroke="#111" stroke-width="4"/>
    <path d="M22 20 Q44 8 66 20 L60 28 Q44 22 28 28 Z" fill="#111"/>
    <rect x="26" y="32" width="36" height="20" rx="4" fill="#111"/>
  </svg>
  <div class="abs tel">0120-731-904</div>
  <div class="abs hours">受付 9:00～18:00<br>除外（日・3が日除く）</div>
  <div class="abs center">グリーンウェーブ受付センター<span>埼玉県加須市松葉912</span></div>

</div>
</body>
</html>
```